Harbor Nightclub

Nightclub flyer., digital single sided, for KV and PX. I included samples of some previous flyers we've used. Sample Info:
HARBOR
FRIDAYS
FRI MAY 1 2020
DJ VORTAN (club floor)
DJ RUZO & DJ TAV (residents on the lounge floor)
4217 Marlow Avenue Sacramento
www.harborvenuehall.example for list/VIP inquiries

Target Market(s)

Upscale top 40 crowd but want some cool and artsy like the examples included.

Font styles to use
Sans Serif

Requirements
Must have
• Harbor Logo
Nice to have
• Would be nice if the flyer can be incorporated later with DJ photos (sometimes we will add dj photos to pixagram etc). Would like a big city type of feel.
Should not have
• Nothing too sexual.

```html
<!DOCTYPE html>
<html lang="en">
<head>
<meta charset="utf-8">
<title>Harbor Fridays Flyer</title>
<link rel="stylesheet" href="https://fonts.googleapis.com/css2?family=Graduate&family=Antic+Didone&family=Roboto+Condensed:wght@400&family=Cinzel:wght@400&family=Cormorant+SC:wght@500&display=swap">
<style>
  :root {
    --night-deep: #05080c;
    --night-mid: #13202a;
    --night-glow: #2a3a3e;
    --neon-white: #f4ffff;
    --neon-cyan: #35e0e8;
    --ring-teal: #1fb3b8;
    --accent-yellow: #f1dc12;
    --date-yellow: #f2d51a;
    --ink-black: #000000;
    --text-white: #ffffff;
    --logo-grey: #9a9a9a;
  }
  html, body {
    margin: 0;
    padding: 0;
    width: 1200px;
    height: 1200px;
    overflow: hidden;
    background: var(--ink-black);
  }
  .flyer {
    position: relative;
    width: 1200px;
    height: 1200px;
    overflow: hidden;
  }
  .flyer svg { display: block; }
  .headline {
    font-family: "Graduate", serif;
    fill: var(--neon-white);
    filter: url(#neon-glow);
  }
  .event-date {
    font-family: "Antic Didone", serif;
    fill: var(--date-yellow);
  }
  .dj-name {
    font-family: "Graduate", serif;
    fill: var(--text-white);
  }
  .dj-name .amp { fill: var(--date-yellow); }
  .dj-room {
    font-family: "Graduate", serif;
    fill: var(--text-white);
  }
  .list-band-text {
    font-family: "Roboto Condensed", sans-serif;
    fill: var(--ink-black);
  }
  .venue-name {
    font-family: "Cinzel", serif;
    fill: var(--text-white);
  }
  .venue-address {
    font-family: "Cormorant SC", serif;
    fill: var(--text-white);
  }
</style>
</head>
<body>
<main class="flyer">
  <svg width="1200" height="1200" viewBox="0 0 1200 1200" xmlns="http://www.w3.org/2000/svg">
    <defs>
      <linearGradient id="skyline-tone" x1="0" y1="0" x2="0" y2="1">
        <stop offset="0" stop-color="var(--night-deep)"/>
        <stop offset="0.45" stop-color="var(--night-mid)"/>
        <stop offset="1" stop-color="var(--night-glow)"/>
      </linearGradient>
      <radialGradient id="skyline-light" cx="0.5" cy="0.45" r="0.6">
        <stop offset="0" stop-color="#3a4a50" stop-opacity="0.45"/>
        <stop offset="1" stop-color="#000" stop-opacity="0"/>
      </radialGradient>
      <filter id="neon-glow" x="-20%" y="-40%" width="140%" height="180%">
        <feGaussianBlur in="SourceAlpha" stdDeviation="7" result="blur"/>
        <feFlood flood-color="#35e0e8" flood-opacity="0.9"/>
        <feComposite in2="blur" operator="in" result="glow"/>
        <feMerge>
          <feMergeNode in="glow"/>
          <feMergeNode in="glow"/>
          <feMergeNode in="SourceGraphic"/>
        </feMerge>
      </filter>
      <filter id="ring-blur" x="-20%" y="-20%" width="140%" height="140%">
        <feGaussianBlur stdDeviation="6"/>
      </filter>
    </defs>

    <!-- city backdrop -->
    <g class="city-backdrop" role="img" aria-label="Night city skyline with lit skyscrapers">
      <rect x="0" y="0" width="1200" height="851" fill="url(#skyline-tone)"/>
      <rect x="0" y="0" width="1200" height="851" fill="url(#skyline-light)"/>
    </g>

    <!-- teal halo ring -->
    <circle class="halo-ring" cx="600" cy="380" r="500" fill="none" stroke="var(--ring-teal)" stroke-width="14" stroke-opacity="0.45" filter="url(#ring-blur)"/>
    <circle class="halo-ring-core" cx="600" cy="380" r="500" fill="none" stroke="var(--ring-teal)" stroke-width="3" stroke-opacity="0.5"/>

    <!-- headline -->
    <text class="headline" x="345" y="307" font-size="186" textLength="517" lengthAdjust="spacingAndGlyphs">HARBOR</text>
    <text class="headline" x="337" y="483" font-size="176" textLength="533" lengthAdjust="spacingAndGlyphs">FRIDAYS</text>

    <text class="event-date" x="385" y="558" font-size="60" textLength="430" lengthAdjust="spacingAndGlyphs">FRIDAY MAY 1 2020</text>

    <!-- line-up -->
    <text class="dj-name" x="85" y="720" font-size="64" textLength="392" lengthAdjust="spacingAndGlyphs">DJ VORTAN</text>
    <text class="dj-room" x="300" y="773" font-size="30" textLength="177" lengthAdjust="spacingAndGlyphs">CLUB FLOOR</text>

    <text class="dj-name" x="642" y="798" font-size="68" textLength="520" lengthAdjust="spacingAndGlyphs">DJ RUZO <tspan class="amp">&amp;</tspan> DJ TAV</text>
    <text class="dj-room" x="642" y="852" font-size="34" textLength="398" lengthAdjust="spacingAndGlyphs">RESIDENTS ON THE LOUNGE</text>

    <!-- list band -->
    <rect class="list-band" x="0" y="862" width="1200" height="80" fill="var(--accent-yellow)"/>
    <text class="list-band-text" x="600" y="914" font-size="34" text-anchor="middle">Visit www.harborvenuehall.example for List/VIP Inquiries</text>

    <!-- venue footer -->
    <rect class="footer" x="0" y="942" width="1200" height="258" fill="var(--ink-black)"/>
    <circle class="venue-mark" cx="600" cy="995" r="34" fill="var(--logo-grey)"/>
    <text class="venue-name" x="600" y="1083" font-size="42" text-anchor="middle" letter-spacing="2">HARBOR</text>
    <text class="venue-address" x="600" y="1134" font-size="25" text-anchor="middle" letter-spacing="1">4217 Marlow Avenue Sacramento</text>
  </svg>
</main>
</body>
</html>
```